Flyer-Design für Eröffnung des Salons Belle Rivane gesucht
Zielgruppe
Es soll sehr gut mit meinem Website harmonisieren.
www.belle-rivane.ch
Aufgabenstellung
Ich eröffne einen Kosmetiksalon und wünsche mir einen schönen Flyer zur Ankündigung der Eröffnung. Bitte in A5 im Hochformat erstellen.
Der Flyer soll auch einen Gutschein für eine Gesichtsbehandlung im Wert von 30 Chf enthalten (nach Möglichkeit rechts oben auf dem Flyer, in einer gut sichtbaren Farbe).
Auf den Seiten des Flyers wünsche ich einfache Abschlüsse mit sanften Farben oder in Schwarz-weissem Grauton Blumendesign.
Der ganze Flyer soll eher simple wirken und dennoch ein Blickfang sein,darf nicht kitschig auffallen sondern soll Klasse und Edel wirken.
Mittig soll Platz sein fur vier Linien Text,d.h ein noch nicht ganz definiertes Angebot für drei Arten von Gesichtsbehandlungen und eiem speziellen Angebot. Im moment können noch Fantasietexte als Platzhalter dienen.

```html
<!DOCTYPE html>
<html lang="de">
<head>
<meta charset="utf-8">
<title>Belle Rivane – Neueröffnung Flyer</title>
<link rel="stylesheet" href="https://fonts.googleapis.com/css2?family=Jost:wght@300;400;500;600;700&display=swap">
<style>
  :root {
    --sky: #7ccbe0;
    --sky-deep: #5dbfdf;
    --taupe: #8c7c72;
    --ink: #111111;
    --paper: #ffffff;
    --page-edge: rgba(0,0,0,0.12);
    --partner: #d9d4cf;
  }
  * { box-sizing: border-box; margin: 0; padding: 0; }
  html, body { width: 1200px; height: 848px; overflow: hidden; background: var(--paper); }
  body { position: relative; font-family: "Jost", sans-serif; }

  .flyer {
    position: absolute; top: 116px; width: 423px; height: 600px;
    overflow: hidden; box-shadow: 0 0 2px var(--page-edge);
  }
  .flyer--front { left: 138px; }
  .flyer--back { left: 632px; background: var(--paper); }

  /* Front */
  .headline-band {
    position: absolute; left: 0; top: 0; width: 100%; height: 53px;
    background: var(--sky); color: var(--paper);
    font-weight: 400; font-size: 38px; letter-spacing: 3px;
    text-align: center; line-height: 55px;
  }
  .portrait {
    position: absolute; left: 0; top: 53px; width: 100%; height: 547px;
    background: radial-gradient(ellipse at 30% 40%, #bdbdbd 0%, #8d8d8d 35%, #4a4a4a 70%, #2a2a2a 100%);
  }
  .brand {
    position: absolute; left: 261px; top: 258px; width: 150px; text-align: center;
  }
  .brand__name { color: var(--paper); font-size: 24px; font-weight: 300; letter-spacing: 0.5px; display: block; }
  .brand__web { color: var(--paper); font-size: 6px; letter-spacing: 1.2px; display: block; margin-top: 6px; }
  .voucher__value {
    position: absolute; left: 264px; top: 320px; width: 159px;
    color: var(--paper); font-weight: 700; font-size: 42px; line-height: 1;
    white-space: nowrap;
  }
  .voucher__band {
    position: absolute; left: 252px; top: 371px; width: 171px; height: 22px;
    background: var(--sky); color: var(--paper);
    font-weight: 500; font-size: 15px; letter-spacing: 1.5px; line-height: 23px; padding-left: 11px;
    white-space: nowrap;
  }
  .voucher__line { position: absolute; left: 252px; width: 171px; height: 1px; background: var(--paper); }
  .copyright {
    position: absolute; left: 412px; top: 598px; transform-origin: 0 0; transform: rotate(-90deg);
    color: var(--paper); font-size: 4.5px; white-space: nowrap;
  }

  /* Back */
  .menu { position: absolute; left: 14px; right: 14px; top: 10px; }
  .menu__title { font-size: 14.5px; font-weight: 600; color: var(--ink); margin-bottom: 5px; }
  .treatment { margin-bottom: 9px; }
  .treatment__head {
    display: flex; justify-content: space-between;
    color: var(--sky-deep); font-size: 15px; font-weight: 600; line-height: 17px;
  }
  .treatment__desc {
    color: var(--taupe); font-size: 9px; font-weight: 300; line-height: 12px;
    text-align: justify; text-transform: uppercase;
  }
  .service-list { position: absolute; left: 14px; right: 14px; top: 240px; list-style: none; }
  .service {
    display: flex; justify-content: space-between; font-size: 15px; font-weight: 600; height: 29px; line-height: 20px;
  }
  .service:nth-child(3) { height: 30px; }
  .service__name { color: var(--ink); }
  .service__price { color: var(--sky-deep); }
  .back-brand { position: absolute; left: 14px; top: 505px; }
  .back-brand__name { color: var(--taupe); font-size: 44px; font-weight: 300; display: block; line-height: 1; white-space: nowrap; }
  .back-brand__web { color: var(--taupe); font-size: 9px; letter-spacing: 2px; display: block; margin: 14px 0 0 31px; white-space: nowrap; }
  .partners { position: absolute; left: 295px; top: 532px; width: 114px; }
  .partner { position: absolute; background: var(--partner); }
</style>
</head>
<body>
  <section class="flyer flyer--front">
    <div class="portrait" role="img" aria-label="Schwarz-weiss Porträtfoto einer lächelnden Frau mit handgeschriebenem Schriftzug „Oui, c'est moi.“"></div>
    <h1 class="headline-band">NEUERÖFFNUNG</h1>
    <div class="brand">
      <span class="brand__name">Belle Rivane</span>
      <span class="brand__web">WWW.BELLE-RIVANE.CH</span>
    </div>
    <div class="voucher__value">30 CHF</div>
    <div class="voucher__band">GUTSCHEIN FÜR</div>
    <div class="voucher__line" style="top:428px"></div>
    <div class="voucher__line" style="top:461px"></div>
    <div class="voucher__line" style="top:493px"></div>
    <div class="copyright">© Clarenne GmbH. All rights reserved.</div>
  </section>

  <section class="flyer flyer--back">
    <div class="menu">
      <h2 class="menu__title">GESICHTSBEHANDLUNGEN</h2>
      <div class="treatment">
        <div class="treatment__head"><span>KURZBEHANDLUNG</span><span>99 CHF</span></div>
        <p class="treatment__desc">Reinigung, Peeling, Ausreinigung, Augenbrauenkorrektur, beruhigende Maske, Abschlusspflege.</p>
      </div>
      <div class="treatment">
        <div class="treatment__head"><span>KLASSISCHE GESICHTSBEHANDLUNG</span><span>129 CHF</span></div>
        <p class="treatment__desc">Reinigung, Peeling (mit oder ohne Dampf), Ausreinigung, Brauenkorrektur, Essencen-Massage, Mask, Abschlusspflege.</p>
      </div>
      <div class="treatment">
        <div class="treatment__head"><span>SOIN THALASSO</span><span>139 CHF</span></div>
        <p class="treatment__desc">Feuchtigkeitsbehandlung mit vitalisierender Algenmaske Reinigung, Peeling, Ausreinigung, Essence-Massage, Algenmaske, Abschlusspflege.</p>
      </div>
      <div class="treatment">
        <div class="treatment__head"><span>ANTI-AGING BEHANDLUNG</span><span>149 CHF</span></div>
        <p class="treatment__desc">Reinigung, Enzympeeling, Ausreinigung, Brauenkorrektur, Caviar Essence, Massage, Trüffelmaske, Abschlusspflege.</p>
      </div>
    </div>
    <ul class="service-list">
      <li class="service"><span class="service__name">HAARENTFERNUNG ab</span><span class="service__price">149 CHF</span></li>
      <li class="service"><span class="service__name">KOSMETISCHE FUSSPFLEGE ab</span><span class="service__price">30 CHF</span></li>
      <li class="service"><span class="service__name">WIMPERNVERLÄNGERUNG ab</span><span class="service__price">119 CHF</span></li>
      <li class="service"><span class="service__name">BEAUTY FOR MEN ab</span><span class="service__price">39 CHF</span></li>
    </ul>
    <div class="back-brand">
      <span class="back-brand__name">Belle Rivane</span>
      <span class="back-brand__web">WWW.BELLE-RIVANE.CH</span>
    </div>
    <div class="partners" aria-label="Partnermarken">
      <div class="partner" style="left:40px;top:0;width:74px;height:14px"></div>
      <div class="partner" style="left:0;top:22px;width:56px;height:18px"></div>
      <div class="partner" style="left:66px;top:22px;width:48px;height:18px"></div>
    </div>
  </section>
</body>
</html>
```